Very High End Grooming Salon needs new business card design

I need a very nice card design I am a certified Master groomer we have a very high end clients. Our color is pink but does not have to be pink. I have a logo also a mission statement .
Fluff N Fern Pet Boutique and Spa
48810 Marlow Rd
North Palm Beach fl 33471
561 904 3782
www.fluffernboutique.example
online booking available
this is our mission statement not sure it need to go on card but here it is.
Our Mission is to show respect to all animals pampering them with the same high end tailored service one would expect to receive at a day spa
as the only certified master groomer in the area we strive to put your pets best paw forward.

Industry/Entity Type

Business

```html
<!DOCTYPE html>
<html lang="en">
<head>
<meta charset="utf-8">
<title>Fluff N Fern – Business Card</title>
<link rel="stylesheet" href="https://fonts.googleapis.com/css2?family=Cabin:wght@400;500&family=Arimo&display=swap">
<style>
  :root {
    --sheet: #ffffff;
    --sheet-edge: #b5b5b5;
    --card: #060606;
    --pink: #d8317c;
    --pink-soft: #e98fb5;
    --pink-pale: #f2b3cf;
    --ink: #111111;
  }
  html, body {
    margin: 0;
    padding: 0;
    width: 1200px;
    height: 1133px;
    overflow: hidden;
    background: var(--sheet);
  }
  .sheet {
    position: relative;
    width: 1200px;
    height: 1133px;
    box-sizing: border-box;
    border: 2px solid var(--sheet-edge);
    background: var(--sheet);
    font-family: "Cabin", sans-serif;
  }
  .dimension {
    position: absolute;
    font-family: "Arimo", sans-serif;
    color: var(--ink);
    font-size: 29px;
    line-height: 1;
  }
  .dimension-width {
    left: 119px;
    top: 92px;
    width: 733px;
    height: 30px;
  }
  .dimension-width .rule {
    position: absolute;
    left: 0;
    right: 0;
    top: 14px;
    border-top: 3px dashed var(--ink);
  }
  .dimension-width .label {
    position: absolute;
    left: 50%;
    top: 0;
    transform: translateX(-50%);
    background: var(--sheet);
    padding: 0 12px;
  }
  .dimension-height {
    left: 100px;
    top: 139px;
    width: 34px;
    height: 400px;
  }
  .dimension-height .rule {
    position: absolute;
    top: 0;
    bottom: 0;
    left: 14px;
    border-left: 3px dashed var(--ink);
  }
  .dimension-height .label {
    position: absolute;
    left: 16px;
    top: 50%;
    transform: translate(-50%, -50%) rotate(-90deg);
    background: var(--sheet);
    padding: 0 12px;
    white-space: nowrap;
  }
  .side-label {
    position: absolute;
    left: 879px;
    font-family: "Arimo", sans-serif;
    font-size: 61px;
    color: var(--ink);
    line-height: 1;
  }
  .side-label-front { top: 342px; }
  .side-label-back { top: 790px; }

  .card {
    position: absolute;
    left: 139px;
    width: 703px;
    height: 430px;
    background: var(--card);
    color: var(--pink);
  }
  .card-front { top: 132px; }
  .card-back { top: 614px; }

  .contact {
    position: absolute;
    left: 20px;
    top: 130px;
    width: 340px;
    margin: 0;
    text-align: center;
    font-size: 20px;
    line-height: 27.5px;
    font-weight: 500;
    font-style: normal;
  }
  .contact span { display: block; }

  .brand-name {
    position: absolute;
    left: 396px;
    top: 18px;
    width: 290px;
    text-align: center;
    font-size: 38px;
    font-weight: 500;
    color: var(--pink);
    margin: 0;
  }
  .mascot-art {
    position: absolute;
    left: 382px;
    top: 72px;
    width: 300px;
    height: 300px;
    border-radius: 46% 40% 38% 44%;
    background: radial-gradient(circle at 45% 45%, var(--pink-pale) 0%, var(--pink-soft) 55%, var(--pink) 100%);
    opacity: 0.9;
  }
  .tagline {
    position: absolute;
    left: 396px;
    top: 382px;
    width: 290px;
    text-align: center;
    font-size: 24px;
    font-variant: small-caps;
    letter-spacing: 0.5px;
    margin: 0;
  }
  .back-url {
    position: absolute;
    left: 0;
    right: 0;
    top: 198px;
    margin: 0;
    text-align: center;
    padding-right: 110px;
    font-size: 25px;
    font-weight: 500;
  }
</style>
</head>
<body>
<main class="sheet">
  <div class="dimension dimension-width">
    <div class="rule"></div>
    <span class="label">9 cm</span>
  </div>
  <div class="dimension dimension-height">
    <div class="rule"></div>
    <span class="label">5,5 cm</span>
  </div>

  <section class="card card-front" aria-label="Card front">
    <address class="contact">
      <span>Fluff N Fern Pet Boutique and Spa</span>
      <span>48810 Marlow Rd</span>
      <span>North Palm Beach fl 33471</span>
      <span>561 904 3782</span>
      <span>www.fluffernboutique.example</span>
      <span>online booking available</span>
    </address>
    <div class="mascot-art" role="img" aria-label="Illustration of a pink poodle decorated with swirls"></div>
    <p class="brand-name">Fluff N Fern</p>
    <p class="tagline">Pet Boutique and Spa</p>
  </section>
  <div class="side-label side-label-front">FRONT</div>

  <section class="card card-back" aria-label="Card back">
    <p class="back-url">www.fluffernboutique.example</p>
  </section>
  <div class="side-label side-label-back">BACK</div>
</main>
</body>
</html>
```